Construction Company Business Card

Business Card Design using new Logo

Contact Information for Business Card

include all company info and website

Requirements
Must have
• Wesley Corman - President
ph. 254-617-0382
Cedar Knoll, TX
wesley@ironmarkframing.com
www.ironmarkframing.com

```html
<!DOCTYPE html>
<html lang="en">
<head>
<meta charset="utf-8">
<title>Ironmark Framing – Business Card</title>
<link rel="stylesheet" href="https://fonts.googleapis.com/css2?family=Montserrat:wght@400;500;700&display=swap">
<style>
  :root {
    --bg: #1e1e1e;
    --paper: #ffffff;
    --brand-red: #c02126;
    --brand-grey: #b9bbbf;
    --stripe-grey: #c4c6cc;
    --ink-white: #ffffff;
  }
  * { box-sizing: border-box; margin: 0; padding: 0; }
  html, body {
    width: 1200px; height: 780px; overflow: hidden;
    background: var(--bg);
    font-family: "Montserrat", Arial, sans-serif;
  }
  .sheet {
    position: relative; width: 1200px; height: 780px;
    display: flex; align-items: center; justify-content: center; gap: 48px;
  }
  .card {
    position: relative; width: 540px; height: 310px;
    background: var(--paper); overflow: hidden;
    box-shadow: 0 10px 30px rgba(0,0,0,.45);
  }

  /* Wordmark */
  .wordmark {
    display: flex; align-items: center; gap: 10px;
    color: var(--brand-grey); font-weight: 500;
    letter-spacing: .12em; text-transform: uppercase;
  }
  .wordmark__dot { width: 10px; height: 10px; background: var(--brand-red); }
  .rule { height: 1px; background: var(--brand-red); }

  /* Front */
  .card--front .front__brand {
    position: absolute; left: 0; right: 0; top: 96px;
    display: flex; flex-direction: column; align-items: center; gap: 12px;
  }
  .card--front .wordmark { font-size: 26px; }
  .card--front .rule { width: 330px; }
  .front__web {
    position: absolute; left: 0; right: 0; top: 218px;
    display: flex; align-items: center; justify-content: center; gap: 14px;
    font-size: 15px; color: var(--brand-grey); letter-spacing: .04em;
  }
  .front__web .domain { color: var(--brand-red); }
  .front__web .dash { width: 26px; height: 1px; background: var(--brand-grey); }

  /* Back */
  .back__brand {
    position: absolute; left: 0; top: 0; width: 250px; height: 100%;
    display: flex; flex-direction: column; justify-content: center; align-items: center; gap: 10px;
  }
  .back__brand .wordmark { font-size: 17px; gap: 8px; }
  .back__brand .wordmark__dot { width: 8px; height: 8px; }
  .back__brand .rule { width: 200px; }
  .back__stripe {
    position: absolute; left: 250px; top: 0; width: 8px; height: 100%;
    background: var(--stripe-grey);
  }
  .back__panel {
    position: absolute; left: 258px; top: 0; right: 0; height: 100%;
    background: var(--brand-red); color: var(--ink-white);
    padding: 62px 0 0 40px;
  }
  .back__notch {
    position: absolute; left: 250px; top: 78px; width: 0; height: 0;
    border-top: 8px solid transparent; border-bottom: 8px solid transparent;
    border-left: 10px solid var(--stripe-grey);
  }
  .person__name { font-size: 25px; font-weight: 400; letter-spacing: .02em; line-height: 1.1; }
  .person__name b { font-weight: 700; }
  .person__role { font-size: 14px; margin-top: 2px; letter-spacing: .03em; }
  .person__place { font-size: 13px; margin-top: 40px; }
  .contact { list-style: none; margin-top: 12px; font-size: 13px; line-height: 1.65; }
  .contact li { display: flex; align-items: center; gap: 8px; }
  .contact svg { width: 11px; height: 11px; fill: var(--ink-white); flex: none; }
</style>
</head>
<body>
<main class="sheet">
  <section class="card card--front" aria-label="Card front">
    <div class="front__brand">
      <div class="wordmark"><span class="wordmark__dot"></span>Ironmark Framing</div>
      <div class="rule"></div>
    </div>
    <p class="front__web">
      <span class="dash"></span>
      <span>www.<span class="domain">ironmarkframing</span>.com</span>
      <span class="dash"></span>
    </p>
  </section>

  <section class="card card--back" aria-label="Card back">
    <div class="back__brand">
      <div class="wordmark"><span class="wordmark__dot"></span>Ironmark Framing</div>
      <div class="rule"></div>
    </div>
    <div class="back__stripe"></div>
    <div class="back__panel">
      <h1 class="person__name"><b>Wesley</b> Corman</h1>
      <p class="person__role">President</p>
      <p class="person__place">Cedar Knoll, TX</p>
      <ul class="contact">
        <li>
          <svg viewBox="0 0 24 24" aria-hidden="true"><path d="M6.6 10.8a15 15 0 0 0 6.6 6.6l2.2-2.2c.3-.3.7-.4 1-.2 1.1.4 2.3.6 3.6.6.6 0 1 .4 1 1V20c0 .6-.4 1-1 1A17 17 0 0 1 3 4c0-.6.4-1 1-1h3.5c.6 0 1 .4 1 1 0 1.3.2 2.5.6 3.6.1.3 0 .7-.2 1z"/></svg>
          254-617-0382
        </li>
        <li>
          <svg viewBox="0 0 24 24" aria-hidden="true"><path d="M2 5h20v14H2z M2 5l10 8 10-8" fill="none" stroke="#fff" stroke-width="2"/></svg>
          wesley@ironmarkframing.com
        </li>
        <li>
          <svg viewBox="0 0 24 24" aria-hidden="true"><circle cx="12" cy="12" r="10"/></svg>
          www.ironmarkframing.com
        </li>
      </ul>
    </div>
    <div class="back__notch"></div>
  </section>
</main>
</body>
</html>
```